Interior Decoration and Concept Store needs a webpage design

Sophisticated website for my business, name Wren Hollow. Wren Hollow is a design service and homewares store run by interior decorator Marion Tulk.

Marion's qualification and work experience as an interior decorator, is able to provide advice and recommendations for interior and exterior concepts, colour consultations, furniture, lighting, decor concepts and products are sourced for individual projects. A re-upholstery service is also provided.

Facebook icon.
Projects page.
Profile page.
Established 2009
Medial page

Industry/Entity Type

Store

```html
<!DOCTYPE html>
<html lang="en">
<head>
<meta charset="utf-8">
<title>Wren Hollow — Interiors &amp; Homewares</title>
<link href="https://fonts.googleapis.com/css2?family=Carlito:wght@400;700&family=Roboto:wght@500;700&family=Arimo:wght@400;700&display=swap" rel="stylesheet">
<style>
  :root {
    --ink: #3a3a3a;
    --text: #4a4a4a;
    --muted: #777;
    --line: #d6d6d6;
    --gold: #d9a91c;
    --orange: #e0962a;
    --green: #6fa53f;
    --brown: #8b4a38;
    --footer-bg: #f3f3f3;
    --footer-top: #dcdcdc;
    --page: #ffffff;
    --arrow: #4b8a2c;
  }
  * { box-sizing: border-box; margin: 0; padding: 0; }
  html, body { width: 1069px; height: 1200px; overflow: hidden; background: var(--page); }
  body { position: relative; font-family: "Carlito", "Calibri", sans-serif; color: var(--text); }
  .abs { position: absolute; }

  /* header */
  .brand { left: 94px; top: 34px; display: flex; align-items: center; gap: 10px; }
  .brand-mark { width: 22px; height: 22px; border-radius: 50%; background: var(--ink); }
  .brand-name { font-size: 36px; font-weight: 400; color: var(--ink); letter-spacing: 1px; }
  .social { left: 865px; top: 33px; display: flex; gap: 5px; }
  .social span { width: 19px; height: 19px; border-radius: 50%; display: block; }
  .nav { left: 567px; top: 69px; display: flex; align-items: center; font-size: 13.5px; color: var(--ink); }
  .nav a { color: inherit; text-decoration: none; padding: 7px 13px; }
  .nav .sep { width: 1px; height: 24px; background: var(--line); margin: 0 11px; }
  .nav .current { border-top: 1px solid var(--line); border-bottom: 1px solid var(--line); }

  /* gallery */
  .tile { position: absolute; }
  .tile-feature { display: flex; align-items: center; justify-content: center; }
  .tile-feature .plus { width: 38px; height: 38px; background: #fff; border-radius: 3px; display: flex; align-items: center; justify-content: center; }

  /* welcome */
  .welcome-title { left: 94px; top: 528px; font-size: 35px; color: var(--ink); font-weight: 400; letter-spacing: .3px; }
  .welcome-title strong { font-weight: 700; }
  .welcome-copy { left: 95px; top: 584px; width: 565px; font-size: 11.8px; line-height: 17.8px; }
  .welcome-copy p + p { margin-top: 17.8px; }
  .more { left: 95px; top: 706px; font-family: "Arimo", sans-serif; font-size: 11px; color: var(--muted); display: flex; align-items: center; gap: 8px; }
  .divider { left: 675px; top: 531px; width: 1px; height: 197px; background: var(--line); }

  .popular-title { left: 700px; top: 530px; font-size: 32px; color: var(--ink); }
  .popular-sub { left: 702px; top: 578px; font-size: 11.5px; color: var(--gold); letter-spacing: .3px; }
  .pop-item { left: 703px; display: flex; gap: 19px; }
  .pop-thumb { width: 67px; height: 51px; }
  .pop-text { font-size: 10.8px; line-height: 14.3px; color: #556; margin-top: 1px; }

  /* promos */
  .promo { top: 788px; height: 167px; overflow: hidden; }
  .promo-title { position: absolute; left: 9px; top: 22px; font-family: "Roboto", sans-serif; font-weight: 700; font-size: 31px; color: #333; letter-spacing: -.3px; }
  .promo-tag { position: absolute; left: 9px; top: 56px; padding: 6px 11px; font-family: "Roboto", sans-serif; font-weight: 700; font-size: 15.5px; color: #fff; letter-spacing: -.2px; }
  .promo-copy { position: absolute; left: 8px; top: 95px; width: 215px; font-family: "Arimo", sans-serif; font-size: 11px; line-height: 16.8px; color: #333; }

  /* footer */
  .footer { left: 0; top: 1008px; width: 1069px; height: 192px; background: var(--footer-bg); border-top: 3px solid var(--footer-top); }
  .f-col { position: absolute; top: 40px; }
  .f-col h3 { font-family: "Roboto", sans-serif; font-weight: 500; font-size: 15.5px; color: #2f2f2f; margin-bottom: 12px; letter-spacing: .1px; }
  .f-col li { list-style: none; font-family: "Arimo", sans-serif; font-size: 11.5px; line-height: 20.6px; color: var(--muted); }
  .newsletter { width: 240px; height: 32px; background: #fff; border: 1px solid #d8d8d8; margin-top: 2px; display: flex; justify-content: flex-end; align-items: center; padding-right: 10px; }
  .follow { margin-top: 20px; display: flex; align-items: center; gap: 12px; font-family: "Roboto", sans-serif; font-weight: 500; font-size: 15.5px; color: #2f2f2f; }
  .follow span { width: 14px; height: 14px; border-radius: 50%; background: #b9b9b9; display: block; }
  .copyright { margin-top: 12px; font-family: "Arimo", sans-serif; font-size: 9.5px; color: #666; }
</style>
</head>
<body>

<header>
  <div class="abs brand"><span class="brand-mark"></span><span class="brand-name">Wren Hollow</span></div>
  <div class="abs social" aria-label="Social links">
    <span style="background:#3a66b8"></span>
    <span style="background:#25a6e0"></span>
    <span style="background:#e4407b"></span>
    <span style="background:#c8232c"></span>
    <span style="background:#2e6fa8"></span>
  </div>
  <nav class="abs nav">
    <a class="current">Home</a><span class="sep"></span>
    <a>About</a><span class="sep"></span>
    <a>Gallery</a><span class="sep"></span>
    <a>Blog</a><span class="sep"></span>
    <a>Contact Us</a>
  </nav>
</header>

<section aria-label="Project gallery">
  <div class="tile tile-feature" role="img" aria-label="Framed abstract artwork under a yellow overlay" style="left:92px;top:124px;width:218px;height:184px;background:linear-gradient(135deg,#f6e27a,#fbe98f 60%,#f3e39a)">
    <div class="plus"><svg width="18" height="18" viewBox="0 0 18 18"><path d="M9 2v14M2 9h14" stroke="#f0cc4a" stroke-width="3"/></svg></div>
  </div>
  <div class="tile" role="img" aria-label="Armchair with a colourful throw beside a window" style="left:92px;top:312px;width:218px;height:183px;background:linear-gradient(160deg,#e8e6e2,#c9c2b8 55%,#9a7d62)"></div>
  <div class="tile" role="img" aria-label="Living room with timber shelving and patterned cushions" style="left:315px;top:124px;width:218px;height:371px;background:linear-gradient(180deg,#f0ede8,#d7b48e 35%,#e8e4de 60%,#b9a99a)"></div>
  <div class="tile" role="img" aria-label="Dining table with an orange vase and black chairs" style="left:539px;top:124px;width:218px;height:184px;background:linear-gradient(180deg,#f4f4f4,#eaeaea 60%,#8c6a4c)"></div>
  <div class="tile" role="img" aria-label="Carved wooden cabinet beside a garden door" style="left:762px;top:124px;width:218px;height:184px;background:linear-gradient(90deg,#d8e0d2,#ebe8e4 45%,#8d7a6a)"></div>
  <div class="tile" role="img" aria-label="Bedroom with shutters, bedside lamp and knitted throw" style="left:539px;top:312px;width:441px;height:183px;background:linear-gradient(120deg,#ededed,#dad5cf 50%,#a89f96)"></div>
</section>

<section aria-label="Welcome">
  <h1 class="abs welcome-title"><strong>WELCOME!</strong> WREN HOLLOW</h1>
  <div class="abs welcome-copy">
    <p>Lorem ipsum dolor sit amet, consec tetuer adipi scing. Praesent vestibu. lum molestie lacuiirhs. Aenean non ummy hendreriau ris. Phasellllus. porta. Fusce suscipit varius mium sociis tot. Lorem ipsum dolor sit amet, consec tetuer adipiscing. Praesent vestibu lum molestie lacuiirhs.</p>
    <p>Aenean non ummy hendreriauris. Phasellllus. porta. Fusce suscipit varius mium sociis totdnatibus et magis dis parturient montes, nascetur ridiculus mus. Nulla dui.</p>
  </div>
  <div class="abs more">more <svg width="12" height="12" viewBox="0 0 12 12"><circle cx="6" cy="6" r="6" fill="#444"/><path d="M3 6h5M6 3.5 8.5 6 6 8.5" stroke="#fff" stroke-width="1.5" fill="none"/></svg></div>
  <div class="abs divider"></div>
</section>

<aside aria-label="Most popular">
  <h2 class="abs popular-title" style="font-weight:400">Most popular</h2>
  <div class="abs popular-sub">LOREM IPSUM DOLOR SIT AMET,</div>
  <div class="abs pop-item" style="top:607px">
    <div class="pop-thumb" role="img" aria-label="Fireplace in a white room" style="background:linear-gradient(90deg,#f1ede8,#7a3a1a 50%,#efe9e2)"></div>
    <p class="pop-text">Lorem ipsum dolor sit amet,<br>consec tetuer adipiscing.<br>Praesent vestibu.</p>
  </div>
  <div class="abs pop-item" style="top:675px">
    <div class="pop-thumb" role="img" aria-label="Floral patterned cushions" style="background:linear-gradient(135deg,#e9d36a,#e98aa0 45%,#3b8fb0)"></div>
    <p class="pop-text">Lorem ipsum dolor sit amet,<br>consec tetuer adipiscing.<br>Praesent vestibu.</p>
  </div>
</aside>

<section aria-label="Flooring offers">
  <div class="abs promo" role="img" aria-label="Light timber dining room" style="left:87px;width:271px;background:linear-gradient(100deg,#f7f4ee 35%,#e6d3b0 70%,#cdb48a)">
    <div class="promo-title">HARDWOOD</div>
    <div class="promo-tag" style="background:var(--orange)">GET UP TO 20% OFF</div>
    <p class="promo-copy">Excepteur sint occaecat cupidatat non proident, sunt in culpa qui officia deserunt.</p>
  </div>
  <div class="abs promo" role="img" aria-label="Bright kitchen with tiled splashback" style="left:390px;width:276px;background:linear-gradient(100deg,#f6f4f1 35%,#e5ddd3 60%,#b08a6a)">
    <div class="promo-title">CERAMIC</div>
    <div class="promo-tag" style="background:var(--green)">GET UP TO 20% OFF</div>
    <p class="promo-copy">Excepteur sint occaecat cupidatat non proident, sunt in culpa qui officia deserunt.</p>
  </div>
  <div class="abs promo" role="img" aria-label="Kitchen with timber cabinetry and laminate floor" style="left:701px;width:276px;background:linear-gradient(100deg,#f5f3f0 30%,#d9c2a2 60%,#8a7868)">
    <div class="promo-title">LAMINATE</div>
    <div class="promo-tag" style="background:var(--brown)">GET UP TO 20% OFF</div>
    <p class="promo-copy">Excepteur sint occaecat cupidatat non proident, sunt in culpa qui officia deserunt.</p>
  </div>
</section>

<footer class="abs footer">
  <div class="f-col" style="left:118px">
    <h3>INFORMATION</h3>
    <ul><li>About Us</li><li>Customer Service</li><li>Privacy Policy</li><li>Site Map</li></ul>
  </div>
  <div class="f-col" style="left:296px">
    <h3>WHY BUY FROM US</h3>
    <ul><li>Shipping &amp; Returns</li><li>Secure Shopping</li><li>International Shipping</li><li>Affiliates</li></ul>
  </div>
  <div class="f-col" style="left:521px">
    <h3>MY ACCOUNT</h3>
    <ul><li>Sign In</li><li>View Cart</li><li>My Wishlist</li><li>Track My Order</li></ul>
  </div>
  <div class="f-col" style="left:707px">
    <h3>NEWSLETTER</h3>
    <div class="newsletter"><svg width="10" height="14" viewBox="0 0 10 14"><path d="M2 2l5 5-5 5" stroke="var(--arrow)" stroke-width="2.4" fill="none"/></svg></div>
    <div class="follow">FOLLOW US <span></span><span></span><span></span></div>
    <p class="copyright">© 2014 Wren Hollow. All Rights Reserved.</p>
  </div>
</footer>

</body>
</html>
```